https://www.lernwinkel.de - a website for school website in germany for presentation/paper download

we own the webpage https://www.lernwinkel.de and we need a new webdesign (a new website logo is also possible). we want only new images and css, we don´t want to made any change to the HTML code.
we need only new images/color for a new modern look.

we want to have more trust to our user. they have to download presentation/paper
we need template for this sites:
https://www.lernwinkel.de/
https://www.lernwinkel.de/referate/englisch
https://www.lernwinkel.de/forum.php
https://www.lernwinkel.de/forum/insektenhotel/258614
https://www.lernwinkel.de/referat/latein/sokrates/25892
https://www.lernwinkel.de/schule_seminararbeit_fachliste.php?fach=238
and other sites on the website. (take a look around the website)

we don´t like white color for sublines or text. (h1/h2/strong) . in image are white Text OK.

important: we want to chance ONLY the CSS and PICS, we don´t want to remove or chance any HTML code.

after you have made a mockup of the new design and we give you a go, you have to made a package with the IMAGES and the CSS rules (text how we have to chance the current css)

Target Market(s)

Germany, Austria, Switzerland -DACH

Industry/Entity Type

School

Coding

Coded - Design and coding required

Number of Pages Required

5+ page

Font styles to use
Serif
Sans Serif

Colors

Designer to choose colors to be used in the design.

Requirements
Must have
• We want only to remove images and no HTML Code
Should not have
• NO white colors for Text on the site. In images are OK

```html
<!DOCTYPE html>
<html lang="de">
<head>
<meta charset="utf-8">
<title>Lernwinkel.de – Referate, Hausarbeiten und Community</title>
<link href="https://fonts.googleapis.com/css2?family=Roboto:wght@100;300;400;500&display=swap" rel="stylesheet">
<style>
  :root {
    --brand: #1473c6;
    --brand-dark: #1f3b57;
    --link: #2f6aa8;
    --text: #2a2a2a;
    --muted: #666;
    --line: #dcdcdc;
    --tint: #eef4fb;
    --tint-line: #cfe0f1;
    --green: #3dbb1c;
    --alert: #f04e3e;
    --sky: #4fc3f7;
    --panel-grey: #ececec;
  }
  * { box-sizing: border-box; margin: 0; padding: 0; }
  html, body { width: 1200px; height: 1080px; overflow: hidden; }
  body { font-family: 'Roboto', sans-serif; color: var(--text); background: #fff; position: relative; font-size: 14px; }
  a { color: inherit; text-decoration: none; }
  .page { position: absolute; left: 120px; top: 0; width: 960px; height: 1080px; border-left: 1px solid #f0f0f0; border-right: 1px solid #f0f0f0; }

  .site-header { position: absolute; left: 0; top: 0; width: 960px; height: 70px; background: var(--brand); }
  .brand-name { position: absolute; left: 20px; top: 16px; font-size: 30px; font-weight: 500; color: #fff; letter-spacing: -0.5px; }
  .login-field { position: absolute; top: 14px; width: 144px; height: 42px; background: #fff; border: 1px solid #d6d6d6; display: flex; align-items: center; padding-left: 12px; gap: 7px; font-size: 12px; color: #555; }
  .login-field svg { width: 13px; height: 13px; fill: #555; }
  .login-button { position: absolute; left: 863px; top: 14px; width: 76px; height: 42px; background: var(--brand-dark); color: #fff; font-size: 13px; font-weight: 500; display: flex; align-items: center; justify-content: center; }

  .main-nav { position: absolute; left: 20px; top: 84px; width: 920px; height: 30px; border-bottom: 1px solid var(--line); }
  .main-nav a { position: absolute; top: 2px; font-size: 14px; color: #444; display: flex; align-items: center; gap: 6px; }
  .main-nav svg { width: 12px; height: 12px; fill: #555; }

  .breadcrumb { position: absolute; left: 19px; top: 128px; width: 922px; height: 42px; background: var(--tint); border: 1px solid var(--tint-line); padding: 13px 14px; font-size: 14px; color: #333; }

  .sidebar-left { position: absolute; left: 20px; top: 196px; width: 180px; }
  .side-heading { font-size: 16px; font-weight: 400; color: var(--brand); display: flex; align-items: center; gap: 8px; height: 24px; }
  .side-heading svg { width: 13px; height: 13px; fill: var(--brand); }
  .side-list { list-style: none; margin-top: 7px; }
  .side-list li { height: 37px; border-bottom: 1px solid var(--line); display: flex; align-items: center; gap: 8px; font-size: 14px; color: #222; }
  .side-list li:last-child { border-bottom: none; }
  .side-list svg { width: 11px; height: 11px; fill: #888; }
  .group-community { margin-bottom: 25px; }
  .group-school { margin-bottom: 32px; }
  .stats { width: 180px; border-collapse: collapse; margin-top: 5px; }
  .stats td { height: 37px; border-bottom: 1px solid var(--line); font-size: 14px; }
  .stats tr:last-child td { border-bottom: none; }
  .stats td.value { text-align: right; }
  .new-members { position: absolute; left: 19px; top: 797px; width: 182px; height: 182px; border: 1px solid var(--line); text-align: center; }
  .new-members h3 { font-weight: 400; font-size: 14px; color: var(--brand); margin-top: 24px; display: flex; justify-content: center; gap: 6px; align-items: center; }
  .new-members h3 svg { width: 13px; height: 11px; fill: var(--brand); }
  .avatar { width: 50px; height: 50px; margin: 9px auto 0; }
  .member-name { font-size: 15px; margin-top: 4px; }
  .member-age { font-size: 11px; margin-top: 4px; }
  .profile-link { display: block; font-size: 12px; color: var(--brand); margin-top: 9px; letter-spacing: 0.3px; }

  .content { position: absolute; left: 239px; top: 198px; width: 481px; }
  .search { height: 70px; border-top: 1px solid var(--line); border-bottom: 1px solid var(--line); position: relative; }
  .search-field { position: absolute; left: 0; top: 12px; width: 360px; height: 44px; border: 1px solid #e2e2e2; display: flex; align-items: center; padding-left: 14px; gap: 10px; font-size: 16px; color: #444; }
  .search-field svg { width: 17px; height: 17px; }
  .search-button { position: absolute; left: 366px; top: 13px; width: 115px; height: 43px; background: var(--green); color: #fff; font-size: 15px; font-weight: 500; display: flex; align-items: center; justify-content: center; }
  .hero { margin-top: 21px; width: 481px; height: 323px; background: linear-gradient(180deg, #1572c4 0%, #2a86d2 55%, #1a70bd 100%); }
  .welcome { margin-top: 12px; height: 175px; background: var(--tint); padding: 26px 25px; }
  .welcome h1 { font-weight: 300; font-size: 37px; color: #2a2a2a; line-height: 42px; }
  .welcome p { width: 425px; font-size: 14.5px; line-height: 18px; color: #333; margin-top: 6px; }
  .subjects { margin-top: 22px; padding-left: 4px; }
  .subjects h2 { font-weight: 400; font-size: 14px; color: #444; }
  .subjects p { margin-top: 9px; font-size: 14px; line-height: 22px; color: #555; padding-left: 2px; }
  .subjects a { color: var(--link); }
  .subjects .sep { color: #bbb; margin: 0 7px; }

  .sidebar-right { position: absolute; left: 760px; top: 196px; width: 180px; }
  .messenger-note { font-size: 14.5px; color: #444; line-height: 18px; margin-top: 10px; }
  .messenger-links { font-size: 14px; color: var(--link); margin-top: 9px; }
  .messenger-links span { color: #bbb; }
  .notice { margin-top: 14px; height: 35px; background: var(--alert); color: #fff; font-size: 14px; display: flex; align-items: center; justify-content: center; }
  .promo { margin-top: 14px; height: 384px; position: relative; background: linear-gradient(160deg, #5a5a5a, #7a7a7a 45%, #4a4a4a); }
  .promo-kicker { position: absolute; left: 11px; top: 193px; font-size: 18px; font-weight: 300; color: #fff; }
  .promo-title { position: absolute; left: 11px; top: 222px; font-size: 50px; font-weight: 100; line-height: 45px; color: #fff; }
  .promo-button { position: absolute; left: 13px; top: 331px; width: 153px; height: 40px; background: var(--sky); color: #fff; font-size: 14px; font-weight: 500; display: flex; align-items: center; justify-content: center; }
  .online { height: 34px; background: var(--panel-grey); font-size: 14px; display: flex; align-items: center; gap: 7px; padding-left: 13px; }
  .online svg { width: 12px; height: 10px; fill: #333; }

  .site-footer { position: absolute; left: 20px; top: 1030px; width: 920px; border-top: 1px solid var(--line); padding-top: 15px; display: flex; justify-content: space-between; font-size: 13px; }
  .site-footer .copy { color: #999; }
  .site-footer nav { color: #222; padding-right: 4px; letter-spacing: 0.1px; }
</style>
</head>
<body>
<div class="page">
  <header class="site-header">
    <div class="brand-name">Lernwinkel.de</div>
    <div class="login-field" style="left:551px"><svg viewBox="0 0 12 12"><circle cx="6" cy="3.5" r="3"/><path d="M0 12c0-4 3-5 6-5s6 1 6 5z"/></svg>Username</div>
    <div class="login-field" style="left:707px"><svg viewBox="0 0 12 12"><path d="M3 5V3.5a3 3 0 016 0V5h1v7H2V5zm1.5 0h3V3.5a1.5 1.5 0 00-3 0z"/></svg>Passwort</div>
    <a class="login-button" href="#">LOGIN</a>
  </header>

  <nav class="main-nav">
    <a href="#" style="left:0"><svg viewBox="0 0 12 12"><path d="M6 0l6 6h-2v6H7V8H5v4H2V6H0z"/></svg>Startseite</a>
    <a href="#" style="left:114px"><svg viewBox="0 0 12 12"><circle cx="3" cy="2" r="1.6"/><circle cx="9" cy="2" r="1.6"/><rect x="1" y="4" width="4" height="8"/><rect x="7" y="4" width="4" height="8"/></svg>Community</a>
    <a href="#" style="left:239px"><svg viewBox="0 0 12 12"><path d="M6 0l6 3-6 3-6-3zM0 6l6 3 6-3v2l-6 3-6-3z"/></svg>Referate</a>
    <a href="#" style="left:633px"><svg viewBox="0 0 12 12"><path d="M0 0h9v7H3L0 10zM10 3h2v9l-3-2H4V8h6z"/></svg>Foren</a>
    <a href="#" style="left:722px"><svg viewBox="0 0 12 12"><circle cx="4" cy="4" r="2"/><circle cx="9" cy="4" r="1.7"/><path d="M0 11c0-3 2-4 4-4s4 1 4 4zM8 7c2 0 4 1 4 4H9z"/></svg>Mitglieder</a>
    <a href="#" style="left:839px"><svg viewBox="0 0 12 12"><circle cx="5" cy="5" r="3.5" fill="none" stroke="#555" stroke-width="1.6"/><path d="M7.5 7.5L11.5 11.5" stroke="#555" stroke-width="1.8"/></svg>Flirtsuche</a>
  </nav>

  <div class="breadcrumb">Foren | Mitglieder | Flirtsuche</div>

  <aside class="sidebar-left">
    <div class="group-community">
      <h3 class="side-heading"><svg viewBox="0 0 12 12"><circle cx="3" cy="2" r="1.6"/><circle cx="9" cy="2" r="1.6"/><rect x="1" y="4" width="4" height="8"/><rect x="7" y="4" width="4" height="8"/></svg>Community</h3>
      <ul class="side-list">
        <li><svg viewBox="0 0 12 12"><circle cx="7" cy="4" r="2.5"/><path d="M2 12c0-3 2-4.5 5-4.5s5 1.5 5 4.5zM0 4h4v1.4H0z"/></svg>Registrieren</li>
        <li><svg viewBox="0 0 12 12"><circle cx="4" cy="4" r="2"/><circle cx="9" cy="4" r="1.7"/><path d="M0 11c0-3 2-4 4-4s4 1 4 4zM8 7c2 0 4 1 4 4H9z"/></svg>Mitglieder Login</li>
        <li><svg viewBox="0 0 12 12"><path d="M0 2h8v8H0zM9 2h1v8H9zM11 2h1v8h-1z"/></svg>Foren</li>
        <li><svg viewBox="0 0 12 12"><path d="M0 0h12v9H3L0 12z"/></svg>Chat</li>
        <li><svg viewBox="0 0 12 12"><circle cx="5" cy="5" r="3.5" fill="none" stroke="#888" stroke-width="1.6"/><path d="M7.5 7.5L11.5 11.5" stroke="#888" stroke-width="1.8"/></svg>Flirtsuche</li>
      </ul>
    </div>
    <div class="group-school">
      <h3 class="side-heading"><svg viewBox="0 0 12 12"><path d="M6 1l6 3-6 3-6-3zM2.5 6v3c1 1.5 6 1.5 7 0V6L6 8z"/></svg>Schule &amp; Uni</h3>
      <ul class="side-list">
        <li><svg viewBox="0 0 12 12"><path d="M0 0h12v12H0zM3 3v2h6V3zM3 7v2h6V7z"/></svg>Hausarbeit</li>
        <li><svg viewBox="0 0 12 12"><path d="M0 0h12v12H0zM1.5 1.5v9h9v-9zM3 3h6v1H3zm0 2h6v1H3z"/></svg>Referat</li>
      </ul>
    </div>
    <div>
      <h3 class="side-heading"><svg viewBox="0 0 12 12"><path d="M0 0h12v12H0zM2.5 6v4h1.5V6zm2.8-3v7h1.5V3zm2.8 2v5h1.5V5z"/></svg>Statistik</h3>
      <table class="stats">
        <tr><td>Mitglieder</td><td class="value">401.324</td></tr>
        <tr><td>Männer</td><td class="value">197.694</td></tr>
        <tr><td>Frauen</td><td class="value">196.799</td></tr>
        <tr><td>Referate</td><td class="value">12.458</td></tr>
        <tr><td>Forenbeiträge</td><td class="value">3M+</td></tr>
      </table>
    </div>
  </aside>

  <section class="new-members">
    <h3><svg viewBox="0 0 13 11"><circle cx="8" cy="3" r="2.5"/><path d="M3 11c0-3 2-4.5 5-4.5s5 1.5 5 4.5zM0 4h5v1.4H0zM1.8 2.2h1.4v5H1.8z"/></svg>Neue Mitglieder</h3>
    <svg class="avatar" viewBox="0 0 50 50"><circle cx="25" cy="25" r="25" fill="#e2e2e2"/><circle cx="25" cy="19" r="8" fill="#fff"/><path d="M10 40c3-8 9-11 15-11s12 3 15 11a25 25 0 01-30 0z" fill="#fff"/></svg>
    <div class="member-name">Mondkatze</div>
    <div class="member-age">Alter: 60 Jahre</div>
    <a class="profile-link" href="#">PROFIL</a>
  </section>

  <main class="content">
    <div class="search">
      <div class="search-field"><svg viewBox="0 0 17 17"><circle cx="7" cy="7" r="5.5" fill="none" stroke="#2f6aa8" stroke-width="2"/><path d="M11 11l5 5" stroke="#2f6aa8" stroke-width="2.2"/></svg>Was suchst du? Hier eingeben!</div>
      <a class="search-button" href="#">SUCHEN</a>
    </div>
    <div class="hero" role="img" aria-label="Illustration: aufgeschlagenes Buch, aus dem eine grüne Landschaft mit Fluss, Bäumen und Bergen unter blauem Himmel wächst"></div>
    <section class="welcome">
      <h1>Hallo Besucher,</h1>
      <p>Auf Lernwinkel.de findest du viele Referate, Facharbeiten und Hausaufgaben. Solltest du einmal ein Referat zu einem Thema nicht finden, kannst du deine Frage bei uns im Forum stellen, wo dir in der Regel schnell geholfen wird.</p>
    </section>
    <section class="subjects">
      <h2>Referate - Hausarbeiten - Hausaufgaben zu folgenden Fächern:</h2>
      <p>
        <a href="#">Deutsch</a> (2937)<span class="sep">|</span><a href="#">Englisch</a> (1113)<span class="sep">|</span><a href="#">Latein</a> (275)<span class="sep">|</span><a href="#">Franzoesisch</a> (196)<br>
        <a href="#">|Italienisch</a> (32)<span class="sep">|</span><a href="#">Griechisch</a> (28)<span class="sep">|</span><a href="#">Spanisch</a> (74)<span class="sep">|</span><a href="#">Mathematik</a> (99)<span class="sep">|</span><br>
        <a href="#">Physik</a> (481)<span class="sep">|</span><a href="#">Chemie</a> (450)<span class="sep">|</span><a href="#">Astronomie</a> (82)<span class="sep">|</span><a href="#">Geographie</a> (785)<span class="sep">|</span><br>
        <a href="#">Geschichte</a> (1870)<span class="sep">|</span><a href="#">Sozialkunde</a> (555)<span class="sep">|</span><a href="#">Wirtschaft</a> (435) <a href="#">|Recht</a> (109)<span class="sep">|</span><br>
        <a href="#">Musik</a> (448)<span class="sep">|</span><a href="#">Kunst</a> (265)<span class="sep">|</span><a href="#">Religion</a> (521)<span class="sep">|</span><a href="#">Informatik</a> (191)<span class="sep">|</span><br>
        <a href="#">Hauswirtschaft</a> (109)<span class="sep">|</span><a href="#">Sport</a> (136)<span class="sep">|</span><a href="#">Chor</a> (19)<span class="sep">|</span><a href="#">Biologie</a> (1237)
      </p>
    </section>
  </main>

  <aside class="sidebar-right">
    <h3 class="side-heading"><svg viewBox="0 0 12 12"><path d="M0 0h12v9H3L0 12zM2 2v1.3h8V2zm0 3v1.3h6V5z"/></svg>Live Messenger</h3>
    <p class="messenger-note">Diese Funktion ist nur für Mitglieder verfügbar</p>
    <p class="messenger-links">Mitglieder <span>|</span> Flirtsuche</p>
    <div class="notice">KEINE NEUE NACHRICHT</div>
    <div class="promo" role="img" aria-label="Graues Foto: Lernende vor einem Bücherregal">
      <div class="promo-kicker">Dein lernwinkel.de</div>
      <div class="promo-title">Schon<br>dabei?</div>
      <a class="promo-button" href="#">REGISTRIEREN</a>
    </div>
    <div class="online"><svg viewBox="0 0 12 10"><circle cx="4" cy="3" r="2"/><circle cx="9" cy="3" r="1.7"/><path d="M0 10c0-3 2-4 4-4s4 1 4 4zM8 6c2 0 4 1 4 4H9z"/></svg>204 Mitglieder online</div>
  </aside>

  <footer class="site-footer">
    <span class="copy">© 2017 lernwinkel.de</span>
    <nav>Hauptseite | Referate Schule - Hausarbeit | Impressum | Datenschutz | AGB</nav>
  </footer>
</div>
</body>
</html>
```